Price Calculator as Responsive Web App to support Sales People

We need to build a simple micro web app to support sales people in making quotes. We already have a backend that can take a number of parameters and create a quote. We need put a responsive web app on top of this so that our people on the road can easily do their price simulations.

We need two pages. One for the input and another for the results. No menus, navigations, etc. It is 6 different inputs as shown with boxes in the sketch. They don't need to be boxed, but some of them have a bit of instruction text that clearly need to belong to the input.

This needs to be responsive, but first and foremost designed for smartphones. I have included a background gradient that we would like to use -- or a variant of it. We expect this to be delivered as HTML/CSS + images so that we can quickly write a few pieces of JavaScript ourselves to wire it up to our price simulator.

Industry/Entity Type

Information Technology

Coding

Coded - Design and coding required

Number of Pages Required

2 page

Font styles to use
Sans Serif

Requirements
Must have
• Responsive design
• Easy to wire up JavaScript to the HTML/CSS
Nice to have
• Some quick way to pick number of months. +/- buttons to add remove a year or 3 months. Same thing with number of items. Add 10 or 5 quickly.
• Maybe some parallax effect while scrolling as long as it is not distracting.
Should not have
• Toolbars, Menus, Navigations, Banners, etc. This is just a single micro app.

```html
<!DOCTYPE html>
<html lang="en">
<head>
<meta charset="utf-8">
<title>Engine Power Form</title>
<link rel="stylesheet" href="https://fonts.googleapis.com/css2?family=Roboto+Condensed:wght@400&family=Jost:wght@400;500&family=Lato:wght@700;900&display=swap">
<style>
  :root {
    --bg-deep: #011a33;
    --bg-mid: #033a60;
    --bg-light: #0b4a74;
    --panel: rgba(52, 110, 150, 0.38);
    --panel-border: rgba(190, 215, 235, 0.45);
    --divider: rgba(190, 215, 235, 0.18);
    --highlight: rgba(10, 35, 60, 0.55);
    --step-bg: rgba(60, 115, 155, 0.35);
    --step-border: rgba(170, 205, 230, 0.18);
    --value-bg: #13304d;
    --text: #f2f6fa;
    --text-soft: #dbe6ef;
    --box-border: rgba(220, 232, 242, 0.7);
    --box-fill: #b9c4cf;
    --submit-bg: #0a3d66;
    --footer: #000000;
  }
  * { box-sizing: border-box; margin: 0; padding: 0; }
  html, body { width: 1157px; height: 1200px; overflow: hidden; }
  body {
    position: relative;
    background:
      radial-gradient(ellipse 60% 50% at 30% 40%, rgba(20, 90, 140, 0.55), transparent 70%),
      linear-gradient(135deg, var(--bg-deep) 0%, var(--bg-mid) 35%, var(--bg-light) 55%, var(--bg-mid) 75%, var(--bg-deep) 100%);
    color: var(--text);
    font-family: "Jost", sans-serif;
  }
  .form-title {
    position: absolute; left: 415px; top: -1px; width: 328px; height: 71px;
    border: 1px solid var(--panel-border); border-top: none;
    display: flex; align-items: center; justify-content: center;
    font-family: "Roboto Condensed", sans-serif; font-size: 32px; letter-spacing: 0.5px;
  }
  .stepper {
    position: absolute; left: 156px; width: 846px; height: 58px;
    background: var(--panel); border: 1px solid var(--panel-border);
  }
  .stepper-label {
    position: absolute; left: 0; top: 0; width: 188px; height: 100%;
    border-right: 1px solid var(--divider);
    padding-left: 21px; display: flex; align-items: center;
    font-family: "Roboto Condensed", sans-serif; font-size: 19px;
  }
  .step, .step-value {
    position: absolute; top: 4px; width: 57px; height: 47px;
    display: flex; align-items: center; justify-content: center;
    font-size: 21px;
  }
  .step { background: var(--step-bg); border: 1px solid var(--step-border); }
  .step-value { background: var(--value-bg); border: 1px solid var(--step-border); }
  .step-value.bold { font-family: "Lato", sans-serif; font-weight: 900; font-size: 20px; }
  .step-unit {
    position: absolute; left: 507px; top: 0; height: 100%;
    display: flex; align-items: center;
    font-family: "Lato", sans-serif; font-weight: 900; font-size: 15px;
  }
  .panel {
    position: absolute; left: 156px; width: 846px;
    background: var(--panel); border: 1px solid var(--panel-border);
  }
  .panel-head {
    margin: 0 19px 0 21px; height: 61px;
    border-bottom: 1px solid var(--divider);
    display: flex; align-items: center;
    font-family: "Roboto Condensed", sans-serif; font-size: 19px;
  }
  .checkbox {
    width: 17px; height: 17px; border: 1px solid var(--box-border);
    flex: none; position: relative;
  }
  .checkbox.checked::after {
    content: ""; position: absolute; inset: 3px; background: var(--box-fill);
  }
  .plan-list { list-style: none; margin: 14px 19px 0 16px; }
  .plan {
    height: 42px; margin-bottom: 1px; padding-left: 11px;
    display: flex; align-items: center; gap: 15px;
    font-size: 16.5px; color: var(--text-soft);
  }
  .plan.selected { background: var(--highlight); }
  .plan .sep { margin: 0 8px; }
  .notice { margin: 2px 0 0 27px; font-size: 13px; color: var(--text-soft); }
  .notice strong { font-weight: 500; color: var(--text); }
  .choice-row { position: relative; height: 42px; margin-top: 14px; }
  .choice {
    position: absolute; top: 0; height: 42px;
    display: flex; align-items: center; gap: 15px;
    font-size: 16.5px; color: var(--text-soft);
  }
  .choice.shaded { background: var(--highlight); width: 144px; padding-left: 37px; }
  .choice.strong { font-family: "Lato", sans-serif; font-weight: 700; color: var(--text); }
  .submit {
    position: absolute; left: 857px; top: 1070px; width: 145px; height: 51px;
    background: var(--submit-bg); border: 1px solid var(--panel-border);
    display: flex; align-items: center; justify-content: center; gap: 18px;
    font-family: "Lato", sans-serif; font-weight: 900; font-size: 20px; color: var(--text);
  }
  .submit svg { display: block; }
  .site-footer {
    position: absolute; left: 0; top: 1145px; width: 100%; height: 55px;
    background: var(--footer);
    display: flex; align-items: center; justify-content: center;
    font-size: 11.5px; color: var(--text-soft);
  }
</style>
</head>
<body>
  <h1 class="form-title">ENGINE POWER FORM</h1>

  <section class="stepper" style="top:93px">
    <div class="stepper-label">DURATION</div>
    <div class="step" style="left:251px">-1</div>
    <div class="step" style="left:327px">-12</div>
    <div class="step-value bold" style="left:437px">24</div>
    <div class="step-unit">MONTH</div>
    <div class="step" style="left:603px">+1</div>
    <div class="step" style="left:679px">+12</div>
  </section>

  <section class="stepper" style="top:175px">
    <div class="stepper-label">COUNT</div>
    <div class="step" style="left:251px">-1</div>
    <div class="step" style="left:327px">-10</div>
    <div class="step-value" style="left:437px">100</div>
    <div class="step-unit">ITEMS</div>
    <div class="step" style="left:603px">+1</div>
    <div class="step" style="left:679px">+10</div>
  </section>

  <section class="panel" style="top:257px; height:283px">
    <h2 class="panel-head">ENGINE POWER (BEYOND STANDARD)</h2>
    <ul class="plan-list">
      <li class="plan"><span class="checkbox"></span><span>360 $ / Year<span class="sep">-</span>Bounce Power</span></li>
      <li class="plan selected"><span class="checkbox checked"></span><span>600 $ / Year<span class="sep">-</span>Silver Power</span></li>
      <li class="plan"><span class="checkbox"></span><span>1M $ / Year<span class="sep">-</span>Gold Power</span></li>
      <li class="plan"><span class="checkbox"></span><span>3M $ / Year<span class="sep">-</span>Platinum Power</span></li>
    </ul>
    <p class="notice"><strong>Notic</strong> : Lorem ipsum dolor sit amet, consectetuer adipiscing elit, sed diam nonummy nibh euismod tincidunt ut laoreet dolore</p>
  </section>

  <section class="panel" style="top:558px; height:159px">
    <h2 class="panel-head">SHARED STORAGE ADDITION</h2>
    <div class="choice-row">
      <label class="choice" style="left:27px"><span class="checkbox"></span>10 Kg</label>
      <label class="choice shaded" style="left:175px"><span class="checkbox"></span>50 Kg</label>
      <label class="choice" style="left:392px"><span class="checkbox"></span>100 Kg</label>
      <label class="choice" style="left:581px"><span class="checkbox"></span>500Kg</label>
      <label class="choice" style="left:763px"><span class="checkbox"></span>1T</label>
    </div>
  </section>

  <section class="panel" style="top:734px; height:145px">
    <h2 class="panel-head">ADDITIONAL TIP</h2>
    <div class="choice-row">
      <label class="choice" style="left:27px"><span class="checkbox"></span>15 %</label>
      <label class="choice shaded" style="left:175px"><span class="checkbox"></span>18 %</label>
      <label class="choice" style="left:392px"><span class="checkbox"></span>20 %</label>
    </div>
  </section>

  <section class="panel" style="top:897px; height:145px">
    <h2 class="panel-head">ELASTIC EXTENSION</h2>
    <div class="choice-row">
      <label class="choice strong" style="left:27px"><span class="checkbox"></span>30 %</label>
      <label class="choice shaded strong" style="left:175px"><span class="checkbox"></span>50 %</label>
    </div>
  </section>

  <button class="submit" type="submit">SUBMIT
    <svg width="24" height="26" viewBox="0 0 24 26" aria-hidden="true">
      <rect x="0.5" y="0.5" width="23" height="25" fill="none" stroke="#f2f6fa"/>
      <path d="M9 7 L16 13 L9 19 Z" fill="#f2f6fa"/>
    </svg>
  </button>

  <footer class="site-footer">© 2017 ENGINE POWER FORM &nbsp;|&nbsp; All rights reserved</footer>
</body>
</html>
```